Theme for a ChoreFinch like site for Teenage Entrepreneurs

Design a theme that looks similar to the ChoreFinch.com website that captures some of the look & feel of our live website (Yardlet.com).
We like the idea of illustrated people (cartoon), but are not 100% married to it.

We are building on top of a framework that has an existing structure and fairly usable layout that we also think would be good to retain.
You can view that framework here: https://gigframe.plovatheme.com/

This website is focused on 14 to 18 year old kids who do neighborhood work such as lawn care, cleanup, snow removal, pet care and baby sitting.

Attached is a powerpoint briefing with more specific details as well.

1. Review our live site Yardlet.com
2. Review ChoreFinch.com
3. Review https://gigframe.plovatheme.com
4. Review our uploaded Powerpoint
5. Come up with awesome designs that we should use on our site!

Target Market(s)

Home owners in neighborhoods and 14 to 18 year old male / female entrepreneurs

Font styles to use
Sans Serif

Colors
0792cd
ffffff
fbf289
cfeae6

Requirements
Must have
• Design around the visible functions of the Chorefinch.com and https://gigframe.plovatheme.com websites as a guide.
• Our site must retain those functions for the homeowner and the person doing the work.
Nice to have
• We like the idea of using illustrated people (the cartoon like characters) but we don't 100% need it. We would like to see some designs with illustrated people and without.

```html
<!DOCTYPE html>
<html lang="en">
<head>
<meta charset="UTF-8">
<title>Yardlet – Become a Yardlet</title>
<link rel="stylesheet" href="https://fonts.googleapis.com/css2?family=Quicksand:wght@400;500;600;700&display=swap">
<style>
  :root {
    --brand-blue: #0792cd;
    --heading-blue: #1a8fc8;
    --white: #ffffff;
    --sunny-yellow: #fbf289;
    --mint: #cfeae6;
    --mint-light: #e4f4f1;
    --ink: #3d4446;
    --ink-soft: #5a6466;
    --rule: #b9cfcc;
    --hero-top: #eaf7f0;
    --hero-mid: #d4ecd6;
    --hero-grass: #7cc35a;
    --search-yellow: #f6e04b;
  }
  * { box-sizing: border-box; margin: 0; padding: 0; }
  html, body { width: 1200px; height: 2514px; overflow: hidden; }
  body {
    position: relative;
    font-family: "Quicksand", "Helvetica Neue", Arial, sans-serif;
    color: var(--ink);
    background: var(--mint);
  }
  .section { position: absolute; left: 0; width: 1200px; }
  .section-title {
    position: absolute; left: 0; width: 1200px; text-align: center;
    color: var(--heading-blue); font-weight: 700; letter-spacing: 2px;
    font-size: 31px;
  }
  .pill-button {
    position: absolute; display: flex; align-items: center; justify-content: center;
    background: var(--brand-blue); color: var(--white); border-radius: 30px;
    font-size: 12px; font-weight: 700; letter-spacing: 1px; text-decoration: none;
    box-shadow: 0 3px 6px rgba(7,146,205,.25);
  }

  /* Hero */
  .hero { top: 0; height: 580px; overflow: hidden; }
  .hero-art {
    position: absolute; inset: 0;
    background: linear-gradient(180deg, var(--hero-top) 0%, var(--hero-mid) 62%, #a9d98f 82%, var(--hero-grass) 100%);
  }
  .back-link { position: absolute; left: 106px; top: 46px; width: 66px; height: 42px; }
  .hero-title {
    position: absolute; top: 164px; left: 0; width: 1200px; text-align: center;
    color: var(--brand-blue); font-size: 37px; font-weight: 700; letter-spacing: 2.5px;
  }
  .hero-subtitle {
    position: absolute; top: 218px; left: 0; width: 1200px; text-align: center;
    font-size: 13px; font-weight: 700; letter-spacing: 1px; color: #2d3335;
  }
  .search-bar {
    position: absolute; left: 243px; top: 268px; width: 716px; height: 59px;
    background: var(--white); border-radius: 30px;
    box-shadow: 0 4px 12px rgba(0,0,0,.08);
    display: flex; align-items: center; padding-left: 24px;
    font-size: 14px; color: #555; font-weight: 500;
  }
  .search-button {
    position: absolute; right: 5px; top: 4px; width: 51px; height: 51px; border-radius: 50%;
    background: var(--search-yellow); display: flex; align-items: center; justify-content: center;
  }
  .slider-dots { position: absolute; top: 439px; left: 562px; display: flex; gap: 14px; }
  .slider-dots span { width: 7px; height: 7px; border-radius: 50%; background: rgba(255,255,255,.85); }
  .slider-dots span.active { background: #2d3335; }

  /* What is */
  .about { top: 580px; height: 570px; background: var(--mint); }
  .about .section-title { top: 128px; }
  .about-intro {
    position: absolute; top: 190px; left: 0; width: 1200px; text-align: center;
    font-size: 15px; line-height: 25px; color: var(--ink); font-weight: 500;
  }
  .service-list { position: absolute; top: 303px; left: 0; width: 1200px; height: 170px; }
  .service { position: absolute; width: 180px; text-align: center; }
  .service-art {
    display: block; margin: 0 auto; width: 134px; height: 134px; border-radius: 50%;
    border: 7px solid var(--white); box-shadow: 0 3px 10px rgba(0,0,0,.12);
  }
  .service-name { margin-top: 16px; font-size: 12px; font-weight: 700; letter-spacing: .8px; color: #2d3335; }

  /* How */
  .how { top: 1150px; height: 596px; background: var(--sunny-yellow); }
  .how .section-title { top: 62px; }
  .how-copy {
    position: absolute; left: 137px; top: 256px; width: 290px;
    font-size: 13.5px; line-height: 24px; color: var(--ink); font-weight: 500;
  }
  .how .pill-button { left: 134px; top: 399px; width: 171px; height: 48px; }
  .video-frame {
    position: absolute; left: 459px; top: 154px; width: 573px; height: 347px;
    background: var(--white); padding: 6px;
    box-shadow: 0 4px 14px rgba(0,0,0,.18);
  }
  .video-art {
    width: 100%; height: 100%;
    background: linear-gradient(180deg, #ffffff 0%, #f1f1f1 35%, #e6e4e0 78%, #7fc35e 88%, #6db450 100%);
  }
  .play-button { position: absolute; left: 250px; top: 134px; width: 74px; height: 74px; }

  /* Better */
  .better { top: 1746px; height: 768px; background: linear-gradient(180deg, var(--mint) 0%, var(--mint-light) 100%); }
  .better .section-title { top: 66px; font-size: 33px; }
  .better-art {
    position: absolute; left: 176px; top: 200px; width: 268px; height: 268px; border-radius: 50%;
    background: radial-gradient(circle at 50% 50%, #ffffff 0%, #ffffff 70%, #f3f6f6 100%);
    box-shadow: 0 6px 22px rgba(0,0,0,.1);
  }
  .better-copy {
    position: absolute; left: 531px; top: 250px; width: 390px;
    font-size: 13px; line-height: 24px; color: var(--ink); font-weight: 500;
  }
  .unsure-title {
    position: absolute; top: 512px; left: 0; width: 1200px; text-align: center;
    color: var(--heading-blue); font-size: 22px; font-weight: 700; letter-spacing: 1.2px;
  }
  .unsure-text {
    position: absolute; top: 548px; left: 0; width: 1200px; text-align: center;
    font-size: 16.5px; color: var(--ink-soft); font-weight: 500;
  }
  .better .pill-button { left: 514px; top: 605px; width: 172px; height: 48px; }

  /* Footer */
  .site-footer { position: absolute; top: 2438px; left: 109px; width: 980px; border-top: 1px solid var(--rule); }
  .copyright { position: absolute; top: 29px; left: 0; font-size: 11px; font-weight: 700; color: #2d3335; }
  .footer-links { position: absolute; top: 29px; right: 0; display: flex; gap: 26px; }
  .footer-links a { font-size: 11px; font-weight: 700; color: #2d3335; text-decoration: none; }
</style>
</head>
<body>

<header class="section hero">
  <div class="hero-art" role="img" aria-label="Illustration of two young workers mowing a lawn, one with a push mower and one on a riding mower, over a green hilly backdrop"></div>
  <svg class="back-link" viewBox="0 0 66 42" aria-label="Back">
    <path d="M6 14 L28 2 L26 10 C44 10 60 18 62 38 C54 26 42 22 26 22 L28 30 Z" fill="var(--brand-blue)"/>
  </svg>
  <h1 class="hero-title">BECOME A YARDLET</h1>
  <p class="hero-subtitle">LET US HELP YOU BUILD YOUR TOMORROW!</p>
  <div class="search-bar">
    What chore do you need help with?
    <span class="search-button">
      <svg width="22" height="22" viewBox="0 0 22 22"><circle cx="9" cy="9" r="6.5" fill="none" stroke="#2d3335" stroke-width="2.6"/><line x1="14" y1="14" x2="19.5" y2="19.5" stroke="#2d3335" stroke-width="2.8" stroke-linecap="round"/></svg>
    </span>
  </div>
  <div class="slider-dots"><span class="active"></span><span></span><span></span><span></span></div>
</header>

<section class="section about">
  <h2 class="section-title">WHAT IS A YARDLET?</h2>
  <p class="about-intro">A YARDLET is an aspiring entrepreneur who is looking for exciting new ways to grow and build their business.<br>Some of the services that a Yardlet can offer to do for homeowners are:</p>
  <div class="service-list">
    <div class="service" style="left:124px"><span class="service-art" role="img" aria-label="Lawn care illustration" style="background:linear-gradient(180deg,#bfe6f5 0%,#9fd6ec 50%,#6fbf4e 72%,#5aa83f 100%)"></span><p class="service-name">LAWN CARE</p></div>
    <div class="service" style="left:319px"><span class="service-art" role="img" aria-label="Baby sitting illustration" style="background:linear-gradient(180deg,#3f7f3a 0%,#5c9a45 45%,#e9c84a 70%,#7fae4c 100%)"></span><p class="service-name">BABY SITTING</p></div>
    <div class="service" style="left:520px"><span class="service-art" role="img" aria-label="Household chores illustration" style="background:linear-gradient(180deg,#f1eeea 0%,#e3d9cf 50%,#b06b45 78%,#d7d2cc 100%)"></span><p class="service-name">HOUSEHOLD CHORES</p></div>
    <div class="service" style="left:718px"><span class="service-art" role="img" aria-label="Pet care illustration" style="background:linear-gradient(180deg,#a7c83a 0%,#8cb32e 55%,#7aa028 100%)"></span><p class="service-name">PET CARE</p></div>
    <div class="service" style="left:912px"><span class="service-art" role="img" aria-label="Snow removal illustration" style="background:linear-gradient(180deg,#2f95d3 0%,#3ba2de 60%,#e9f3f8 78%,#ffffff 100%)"></span><p class="service-name">SNOW REMOVAL</p></div>
  </div>
</section>

<section class="section how">
  <h2 class="section-title">HOW DOES IT WORK?</h2>
  <p class="how-copy">YARDLET is a platform to help you build your business from the ground up. It will also help you find jobs in your area by connecting you to local home owners seeking help for various services.</p>
  <a class="pill-button" href="#">LEARN MORE</a>
  <div class="video-frame">
    <div class="video-art" role="img" aria-label="Video still: a man pushing a blue lawn mower in front of a white picket fence"></div>
    <svg class="play-button" viewBox="0 0 74 74" aria-label="Play video">
      <circle cx="37" cy="37" r="34" fill="rgba(255,255,255,.35)" stroke="var(--brand-blue)" stroke-width="4"/>
      <path d="M29 23 L53 37 L29 51 Z" fill="var(--brand-blue)"/>
    </svg>
  </div>
</section>

<section class="section better">
  <h2 class="section-title">WHAT MAKES US BETTER THAN THE NEXT GUY?</h2>
  <div class="better-art" role="img" aria-label="Illustration of a teenager in a cap pushing a lawn mower"></div>
  <p class="better-copy">On top of providing you with a network to find local jobs in your community, we will work with you to help you become an entrepreneur. We will link you to stepping stones such as resources, tools and webinars to build and grow your business. We will also provide a link to a community of other YARDLETS to build business connections in your area.</p>
  <h3 class="unsure-title">STILL NOT SURE?</h3>
  <p class="unsure-text">Connect with other YARDLETS to see how it has helped them grow their businesses!</p>
  <a class="pill-button" href="#">PREVIEW</a>
</section>

<footer class="site-footer">
  <p class="copyright">© 2017 Yardlet &nbsp;|&nbsp; All Rights Reserved</p>
  <nav class="footer-links">
    <a href="#">About Us</a>
    <a href="#">Contact Us</a>
    <a href="#">Press</a>
    <a href="#">Terms &amp; Policy</a>
  </nav>
</footer>

</body>
</html>
```